Tarvel Ridge LLC

Need Professional Business cards for New Investment Fund

Target Market(s)

High Quality investors

Industry/Entity Type

Financial

Contact Information for Business Card

Phone Number +1 555 284 6193
Name Pavel Orlinsky
Title Fund Manager
email po@FundTarvel.example
Website www.FundTarvel.example

Colors

Designer to choose colors to be used in the design.

Requirements
Must have
• Must have our Logo and all of the above. Must be made so lettering and loge can be raised

```html
<!DOCTYPE html>
<html lang="en">
<head>
<meta charset="utf-8">
<title>Tarvel Ridge LLC — Business Card</title>
<link href="https://fonts.googleapis.com/css2?family=Open+Sans:wght@400;600&display=swap" rel="stylesheet">
<style>
  :root {
    --backdrop: #262626;
    --card: #303030;
    --card-edge: #3a3a3a;
    --accent: #5cb947;
    --ink: #f2f2f2;
    --ink-soft: #d6d6d6;
    --silver: #c9c9c9;
  }
  * { box-sizing: border-box; margin: 0; padding: 0; }
  html, body {
    width: 1200px; height: 900px; overflow: hidden;
    background: var(--backdrop);
    font-family: "Open Sans", Arial, sans-serif;
  }
  .stage {
    width: 1200px; height: 900px;
    display: flex; flex-direction: column; align-items: center; justify-content: center;
    gap: 40px;
  }
  .card {
    width: 700px; height: 400px;
    background: var(--card);
    border: 1px solid var(--card-edge);
    box-shadow: 0 14px 30px rgba(0,0,0,0.45);
    position: relative;
  }
  .brand {
    display: flex; align-items: center; gap: 14px;
    font-weight: 600; letter-spacing: 0.04em;
  }
  .brand-mark { width: 22px; height: 22px; }
  .card--back .brand {
    position: absolute; left: 50%; top: 50%; transform: translate(-50%, -50%);
    color: var(--silver); font-size: 38px; white-space: nowrap;
  }
  .card--back .brand-mark { background: var(--silver); }
  .card--front .brand {
    position: absolute; left: 60px; top: 172px;
    color: var(--accent); font-size: 30px; white-space: nowrap;
  }
  .card--front .brand-mark { background: var(--accent); }
  .contact {
    position: absolute; left: 400px; top: 110px;
    color: var(--ink);
  }
  .contact-name { font-size: 24px; font-weight: 600; letter-spacing: 0.03em; }
  .contact-title { font-size: 17px; color: var(--ink-soft); margin-bottom: 22px; letter-spacing: 0.02em; }
  .contact-line { display: flex; align-items: center; gap: 14px; font-size: 19px; margin-bottom: 14px; }
  .contact-line svg { width: 20px; height: 20px; fill: var(--accent); flex: none; }
</style>
</head>
<body>
<main class="stage">
  <section class="card card--back" aria-label="Card back">
    <div class="brand"><span class="brand-mark"></span>Tarvel Ridge LLC</div>
  </section>

  <section class="card card--front" aria-label="Card front">
    <div class="brand"><span class="brand-mark"></span>Tarvel Ridge LLC</div>
    <div class="contact">
      <p class="contact-name">Pavel Orlinsky</p>
      <p class="contact-title">Fund Manager</p>
      <p class="contact-line">
        <svg viewBox="0 0 24 24" aria-hidden="true"><path d="M6.6 10.8a15.1 15.1 0 0 0 6.6 6.6l2.2-2.2c.3-.3.7-.4 1-.2 1.1.4 2.3.6 3.6.6.6 0 1 .4 1 1V20c0 .6-.4 1-1 1A17 17 0 0 1 3 4c0-.6.4-1 1-1h3.5c.6 0 1 .4 1 1 0 1.3.2 2.5.6 3.6.1.3 0 .7-.2 1z"/></svg>
        +1 555 284 6193
      </p>
      <p class="contact-line">
        <svg viewBox="0 0 24 24" aria-hidden="true"><path d="M2 5h20v14H2z M2 5l10 8 10-8" /><path d="M3 6.5v11.5h18V6.5l-9 7z" fill="var(--card)"/></svg>
        po@FundTarvel.example
      </p>
      <p class="contact-line">
        <svg viewBox="0 0 24 24" aria-hidden="true"><circle cx="12" cy="12" r="10"/><path d="M2 12h20M12 2c3 3 3 17 0 20M12 2c-3 3-3 17 0 20" stroke="var(--card)" stroke-width="1.5" fill="none"/></svg>
        www.FundTarvel.example
      </p>
    </div>
  </section>
</main>
</body>
</html>
```